Redesign Company Website WRAPTIDE

We want to redesign the web page of the company using some actual pictures such as the ones that show the production line, equipment and the plant. About the products picture i am ok if upgrade for new ones o keep some of them.
PLease visiti: www.lumodiseno.example.ve/wraptide/ to check the actual page.

Target Market(s)

Processors and Producers of:
Cheese, Fresh Meat, Sausages, Poultry, Processed Meats,

Coding

Coded - Design and coding required

Number of Pages Required

5+ page

Requirements
Must have
• Bilingual Spanish/English
Nice to have

Should not have
• Blogs, or any customer interaction, no particular brand must be shown, must be all generic.

```html
<!DOCTYPE html>
<html lang="en">
<head>
<meta charset="utf-8">
<title>WRAPTIDE – Flexible Packaging</title>
<link href="https://fonts.googleapis.com/css2?family=Nunito:wght@400;600;700&family=Open+Sans:wght@400;600&display=swap" rel="stylesheet">
<style>
:root{
  --teal:#1a9682;
  --teal-dark:#15806f;
  --green-start:#20a17a;
  --green-end:#58b846;
  --leaf:#6aaa2e;
  --text:#333a3a;
  --muted:#777;
  --line:#b9b9b9;
  --white:#ffffff;
  --footer:#0b1f1e;
  --footer-text:#9fb3b1;
}
*{box-sizing:border-box;margin:0;padding:0}
html,body{width:1200px;height:3438px;overflow:hidden}
body{position:relative;background:var(--white);font-family:"Open Sans",Arial,sans-serif;color:var(--text)}
.abs{position:absolute}

/* header */
.brand{left:144px;top:22px;font-family:"Nunito",Arial,sans-serif;font-weight:700;font-size:40px;letter-spacing:3px;color:var(--teal);line-height:46px}
.nav{left:533px;top:36px;display:flex;font-family:"Nunito",Arial,sans-serif;font-size:12.5px;color:#555;text-transform:uppercase}
.nav a{color:inherit;text-decoration:none;margin-right:28px}
.nav a.active{color:var(--teal)}
.lang{left:935px;top:24px;width:120px;height:40px;border:1px solid #bbb;display:flex;align-items:center;padding-left:12px;font-size:12px;color:#555}
.lang .flag{width:20px;height:13px;background:#2a3f8f;margin-right:8px}
.lang .caret{position:absolute;right:14px;top:17px;border-left:5px solid transparent;border-right:5px solid transparent;border-top:6px solid #555}

/* hero */
.hero-photo{left:0;top:89px;width:1200px;height:583px;background:linear-gradient(120deg,#8e7d74 0%,#b9aaa3 25%,#b13a3c 50%,#c44145 70%,#9e3033 100%);clip-path:polygon(0 0,100% 0,100% 100%,627px 100%,600px 525px,0 525px)}
.hero-title{right:145px;top:208px;text-align:right;font-family:"Nunito",Arial,sans-serif;font-weight:600;font-size:32px;line-height:33px;color:var(--white);text-shadow:0 2px 4px rgba(0,0,0,.45)}
.hero-btn{left:928px;top:292px;width:127px;height:44px;background:var(--teal);color:var(--white);font-family:"Nunito",Arial,sans-serif;font-weight:600;font-size:17px;display:flex;align-items:center;justify-content:center}
.arrow{top:332px;width:40px;height:40px;background:var(--leaf);display:flex;align-items:center;justify-content:center}

/* common */
.heading{font-family:"Nunito",Arial,sans-serif;font-weight:600;font-size:33px;line-height:36px;color:var(--teal);text-transform:uppercase}
.copy{font-size:12px;line-height:27.2px;color:var(--text)}
.btn{background:var(--teal);color:var(--white);font-family:"Nunito",Arial,sans-serif;font-size:13px;display:flex;align-items:center;justify-content:center;text-transform:uppercase}

/* welcome */
.welcome-photo{left:144px;top:752px;width:439px;height:360px;background:linear-gradient(135deg,#6b4a2c,#e4c17a 45%,#f1d68c 70%,#8a6238)}
.welcome-title{left:630px;top:747px}
.welcome-copy{left:630px;top:804px;width:430px}
.welcome-btn{left:630px;top:1072px;width:104px;height:40px}

/* green bands */
.band{left:0;width:1200px;background:linear-gradient(90deg,var(--green-start),var(--green-end))}
.band-markets{top:1200px;height:441px;clip-path:polygon(0 0,100% 0,100% 383px,601px 383px,574px 100%,0 100%)}
.band-types{top:2177px;height:569px;clip-path:polygon(0 0,100% 0,100% 100%,626px 100%,599px 512px,0 512px)}
.band-title{width:1200px;left:0;text-align:center;font-family:"Nunito",Arial,sans-serif;font-weight:600;font-size:33px;color:var(--white);text-transform:uppercase}

.market-row{left:144px;top:1328px;display:flex;gap:8px}
.market-card{width:176px;height:175px;background:var(--white);position:relative}
.market-card .icon{position:absolute;left:58px;top:34px;width:60px;height:60px;border-radius:8px;background:#eceeee}
.market-card .label{position:absolute;left:0;right:0;top:128px;text-align:center;font-family:"Nunito",Arial,sans-serif;font-size:16px;color:#333;text-transform:uppercase}

/* chicken & cheeses */
.products-title{left:144px;top:1738px}
.products-copy{left:144px;top:1826px;width:430px}
.products-btn{left:144px;top:2036px;width:104px;height:40px}
.products-photo{left:615px;top:1730px;width:440px;height:359px;background:linear-gradient(135deg,#6b2a2a,#b44a52 40%,#c97577 60%,#5a3a2e)}

/* packaging types */
.type-row{left:144px;top:2313px;display:flex;gap:10px}
.type-card{width:297px;height:297px;background:var(--white);position:relative}
.type-card .shot{position:absolute;left:48px;top:50px;width:200px;height:134px}
.type-card .label{position:absolute;left:0;right:0;top:228px;text-align:center;font-family:"Nunito",Arial,sans-serif;font-size:16px;color:#333;text-transform:uppercase}

/* contact */
.contact-title{left:0;width:1200px;top:2828px;text-align:center}
.field{border:1px solid var(--line);height:39px;font-size:11px;color:var(--muted);padding:13px 15px 0}
.submit{left:555px;top:3143px;width:88px;height:38px}

/* footer */
.footer{left:0;top:3261px;width:1200px;height:177px;background:var(--footer);clip-path:polygon(0 0,574px 0,601px 59px,100% 59px,100% 100%,0 100%)}
.footer-links{left:144px;top:3353px;font-size:11.5px;color:var(--footer-text)}
.footer-links span{margin:0 8px}
.copyright{left:144px;top:3388px;font-size:11.5px;color:var(--footer-text)}
.social{top:3370px;width:20px;height:20px;border-radius:50%;background:var(--footer-text)}
</style>
</head>
<body>

<header>
  <div class="abs brand">WRAPTIDE</div>
  <nav class="abs nav">
    <a class="active" href="#">About</a>
    <a href="#">Markets</a>
    <a href="#">Packaging</a>
    <a href="#">Interest</a>
    <a href="#">Contact</a>
  </nav>
  <div class="abs lang"><span class="flag"></span>English<span class="caret"></span></div>
</header>

<section class="hero">
  <div class="abs hero-photo" role="img" aria-label="Fresh meat cuts on white trays moving along a production conveyor"></div>
  <h1 class="abs hero-title">Vestibulum condimentum<br>risus posuere cursus</h1>
  <div class="abs hero-btn">READ MORE</div>
  <div class="abs arrow" style="left:47px"><svg width="14" height="20" viewBox="0 0 14 20"><path d="M11 2 3 10l8 8" fill="none" stroke="#fff" stroke-width="3"/></svg></div>
  <div class="abs arrow" style="left:1111px"><svg width="14" height="20" viewBox="0 0 14 20"><path d="M3 2l8 8-8 8" fill="none" stroke="#fff" stroke-width="3"/></svg></div>
</section>

<section class="welcome">
  <div class="abs welcome-photo" role="img" aria-label="Assorted cheeses with a cheese knife on a wooden board"></div>
  <h2 class="abs heading welcome-title">Welcome to Wraptide</h2>
  <p class="abs copy welcome-copy">We are a flexible packaging converter company established in Maracaibo, Venezuela. We have 30 years of experience in the flexible packaging market. We were born out of the need of our parent company Quimelar, to create a company focused only on the packaging sector to give the impetus to this business unit which has experienced sustained growth. We maintain strategic alliances with Pakvera (USA) and Brisa Films (Canada), which allows us to be updated with world packaging trends. We are constantly updating technology with new equipment to offer our customers packaging of excellent print quality and innovative shapes.</p>
  <div class="abs btn welcome-btn">Read more</div>
</section>

<section>
  <div class="abs band band-markets"></div>
  <h2 class="abs band-title" style="top:1272px">Etiam vel massa elementum</h2>
  <div class="abs market-row">
    <div class="market-card"><div class="icon" role="img" aria-label="Cheese icon"></div><div class="label">Cheese</div></div>
    <div class="market-card"><div class="icon" role="img" aria-label="Fresh meat icon"></div><div class="label">Fresh meat</div></div>
    <div class="market-card"><div class="icon" role="img" aria-label="Sausages icon"></div><div class="label">Sausages</div></div>
    <div class="market-card"><div class="icon" role="img" aria-label="Poultry icon"></div><div class="label">Poultry</div></div>
    <div class="market-card"><div class="icon" role="img" aria-label="Processed meats icon"></div><div class="label">Processed meats</div></div>
  </div>
</section>

<section>
  <h2 class="abs heading products-title">Chicken and fresh<br>cheeses</h2>
  <p class="abs copy products-copy">Multilayer film with different structures that provide greater shelf-life and maintain the original characteristics of the products. Excellent performance in automatic packaging, with instant sealing and high resistance. It can be smooth or printed in up to eight colors on the latest technology printers, which reproduce packaging with high image resolution and guarantee fideli-ty to the standards approved by the customer. The film is supplied in reels properly packed and palletized, which prevent any contamination.</p>
  <div class="abs btn products-btn">Read more</div>
  <div class="abs products-photo" role="img" aria-label="Raw meat cuts, fresh sausages and ground meat on a board"></div>
</section>

<section>
  <div class="abs band band-types"></div>
  <h2 class="abs band-title" style="top:2249px">Types of packaging</h2>
  <div class="abs type-row">
    <div class="type-card"><div class="shot" role="img" aria-label="Kraft stand-up pouches with windows" style="background:linear-gradient(90deg,#c79a3e,#e2b85a)"></div><div class="label">Self-standing bags</div></div>
    <div class="type-card"><div class="shot" role="img" aria-label="Shrink bags around sausages and meat products" style="background:linear-gradient(90deg,#d8d8d8,#c9352a 40%,#e0662e 75%,#e8c35a)"></div><div class="label">Heart shrinkable bags</div></div>
    <div class="type-card"><div class="shot" role="img" aria-label="Clear vacuum bags with vegetables" style="background:linear-gradient(90deg,#7fae5a,#e2e4e6 45%,#d9dadc 65%,#e6c744)"></div><div class="label">Vaccum bags</div></div>
  </div>
</section>

<section>
  <h2 class="abs heading contact-title">Contact us</h2>
  <div class="abs field" style="left:375px;top:2882px;width:218px">Name</div>
  <div class="abs field" style="left:607px;top:2882px;width:218px">Surname</div>
  <div class="abs field" style="left:375px;top:2938px;width:218px">Email</div>
  <div class="abs field" style="left:607px;top:2938px;width:218px">Phone</div>
  <div class="abs field" style="left:375px;top:2994px;width:450px;height:127px">Message</div>
  <div class="abs btn submit">Submit</div>
</section>

<footer>
  <div class="abs footer"></div>
  <div class="abs footer-links">Home<span>|</span>About<span>|</span>Markets<span>|</span>Packaging<span>|</span>Interest<span>|</span>Contact</div>
  <div class="abs copyright">Copyright © 2020 &nbsp;Wraptide. &nbsp;All rights reserved.</div>
  <div class="abs social" style="left:943px" role="img" aria-label="Social network link"></div>
  <div class="abs social" style="left:987px" role="img" aria-label="Social network link"></div>
  <div class="abs social" style="left:1034px" role="img" aria-label="Social network link"></div>
</footer>

</body>
</html>
```